Tidewell Cryotherapy brochure

I need brochure design for my Cryotherapy business.
Target market: Athletes from high School to pro, Fitness, adults needing relief from arthritic and surgical pain. Color pallet should have be in keeping with the logo blues, white and silver (attached). There should be a sections to address what full body cryo is .. and its benefits, FAQ's. a section that i can list services, prices, hours...ect.. There should also be high quality pics in keeping with the theme of rejuvenation and replenishment. Tri Fold double sided.

Target Market(s)

Target market: Athletes from high School to pro, Fitness, adults needing relief from arthritic and surgical pain.

Industry/Entity Type

Business

Colors
33a6d7
cee9f5
0255a3
cfdeed
ffffff
ecf7fb
d7d7d7
9d9d9d

Requirements
Must have
• There should be a sections to address what full body cryo is .. and its benefits, FAQ's. a section that i can list services, prices, hours...ect.. There should also be high quality pics in keeping with the theme of rejuvenation and replenishment. Tri Fold double sided.
Nice to have
• Graphics of the circulatrory system and cryo's effect on it.

```html
<!DOCTYPE html>
<html lang="en">
<head>
<meta charset="utf-8">
<title>Tidewell Cryotherapy – Tri-Fold Brochure</title>
<link rel="stylesheet" href="https://fonts.googleapis.com/css2?family=Cinzel:wght@400;700&family=Lato:ital,wght@0,400;0,700;0,900;1,400;1,700&display=swap">
<style>
:root{
  --sky:#33a6d7;
  --ice:#cee9f5;
  --navy:#0255a3;
  --deep:#0a2f6e;
  --mist:#cfdeed;
  --white:#ffffff;
  --frost:#ecf7fb;
  --silver:#d7d7d7;
  --steel:#9d9d9d;
  --violet:#4b4aa0;
  --ink:#1d2a44;
  --page:#e9ebee;
}
*{box-sizing:border-box;margin:0;padding:0}
html,body{width:1000px;height:1200px;overflow:hidden;background:var(--page)}
body{font-family:"Lato",Arial,sans-serif;color:var(--ink);position:relative}
.spread{position:absolute;left:130px;width:740px;height:572px;background:var(--white);box-shadow:0 6px 18px rgba(0,0,0,.18);overflow:hidden}
.spread--outside{top:18px}
.spread--inside{top:610px}
.panel{position:absolute;top:0;width:246.67px;height:572px;overflow:hidden}
.panel--1{left:0}.panel--2{left:246.67px}.panel--3{left:493.33px}
.photo{position:absolute}
.wave{position:absolute;left:0;width:100%}
.brand{display:flex;align-items:center;gap:6px;font-family:"Lato",sans-serif;font-weight:900;color:var(--navy);text-transform:uppercase;letter-spacing:.5px;line-height:1;white-space:nowrap}
.brand__dot{width:14px;height:14px;border-radius:50%;background:var(--sky);flex:none}
.faq-title{position:absolute;top:178px;width:100%;text-align:center;font-family:"Cinzel",serif;font-weight:700;font-size:19px;color:var(--navy);letter-spacing:1px}
.faq{position:absolute;left:14px;width:218px;border:1.5px solid var(--violet);border-radius:9px;padding:8px 9px 8px 10px;background:var(--white)}
.faq__icon{position:absolute;left:-10px;top:-6px}
.faq__q{font-family:"Cinzel",serif;font-size:10px;font-weight:700;color:var(--navy);margin:0 0 4px 14px;letter-spacing:.3px}
.faq__a{font-size:7.2px;font-style:italic;font-weight:700;line-height:1.35;color:var(--ink)}
.contact{position:absolute;left:40px;top:392px;list-style:none;color:var(--white);font-size:9px}
.contact li{display:flex;align-items:center;gap:7px;margin-bottom:6px}
.cover-title{position:absolute;top:365px;width:100%;text-align:center}
.cover-title__main{font-family:"Lato",sans-serif;font-weight:900;font-size:27px;color:var(--navy);letter-spacing:.5px}
.cover-title__sub{font-family:"Cinzel",serif;font-size:22px;color:#222;letter-spacing:1px}
.tab{display:inline-block;font-weight:900;font-size:8.5px;text-transform:uppercase;padding:4px 14px 4px 12px;border-radius:0 12px 12px 0;letter-spacing:.3px}
.tab--light{background:var(--white);color:var(--navy)}
.tab--dark{background:var(--navy);color:var(--white)}
.copy{font-size:7.6px;line-height:1.42}
.copy--light{color:var(--white)}
.bullets{list-style:none;font-size:7.6px;line-height:1.4;font-weight:700}
.bullets li{position:relative;padding-left:14px;margin-bottom:6px}
.bullets li::before{content:"";position:absolute;left:2px;top:3px;width:6px;height:6px;border-radius:50%;background:var(--sky)}
.bullets--light{color:var(--white)}
.bullets--dark{color:var(--ink)}
.rates{list-style:none;color:var(--white);font-size:7.5px;font-style:italic}
.rates li{display:flex;align-items:baseline;margin-bottom:3px}
.rates li::after{content:"";order:1;flex:1;border-bottom:1px dotted var(--white);margin:0 4px}
.rates span{order:2;font-style:normal}
.block{position:absolute}
</style>
</head>
<body>

<section class="spread spread--outside" aria-label="Brochure outside">
  <div class="panel panel--1">
    <div class="photo" role="img" aria-label="Photo of a woman relaxing in a cryotherapy chamber with cold mist" style="left:0;top:0;width:100%;height:160px;background:linear-gradient(160deg,#6f86e0 0%,#b9c8f4 45%,#e8eefb 70%,#8ea6e8 100%)"></div>
    <svg class="wave" style="top:110px" width="247" height="80" viewBox="0 0 247 80">
      <path d="M0 60 C70 20 160 5 247 0 L247 80 L0 80Z" fill="#fff"/>
      <path d="M0 58 C70 18 160 3 247 -2" stroke="var(--navy)" stroke-width="5" fill="none"/>
      <path d="M0 66 C80 28 160 14 247 10" stroke="var(--sky)" stroke-width="2" fill="none"/>
    </svg>
    <h2 class="faq-title">FAQS</h2>

    <div class="faq" style="top:212px">
      <svg class="faq__icon" width="22" height="18" viewBox="0 0 22 18"><path d="M2 1h14a2 2 0 0 1 2 2v7a2 2 0 0 1-2 2H8l-4 4v-4H2a2 2 0 0 1-2-2V3a2 2 0 0 1 2-2z" fill="var(--violet)"/><circle cx="6" cy="7" r="1.2" fill="#fff"/><circle cx="9.5" cy="7" r="1.2" fill="#fff"/><circle cx="13" cy="7" r="1.2" fill="#fff"/></svg>
      <h3 class="faq__q">How do I feel after treatment?</h3>
      <p class="faq__a">Your external skin temperature warms up within five minutes of exiting the cryosauna. The immediate effects from each session typically last for six to eight hours. Cryotherapy stimulates the body to release endorphins, which are the hormones that make you feel good and energetic. Most clients report a better night's sleep after just one session!</p>
    </div>

    <div class="faq" style="top:322px">
      <svg class="faq__icon" width="22" height="18" viewBox="0 0 22 18"><path d="M2 1h14a2 2 0 0 1 2 2v7a2 2 0 0 1-2 2H8l-4 4v-4H2a2 2 0 0 1-2-2V3a2 2 0 0 1 2-2z" fill="var(--violet)"/><circle cx="6" cy="7" r="1.2" fill="#fff"/><circle cx="9.5" cy="7" r="1.2" fill="#fff"/><circle cx="13" cy="7" r="1.2" fill="#fff"/></svg>
      <h3 class="faq__q">Is it safe?</h3>
      <p class="faq__a">Yes, it has shown to be both safe and effective for a staggering variety of conditions and goals. Nitrogen is a non-toxic gas that makes up about 78% of the air we breathe; however, breathing pure nitrogen could cause fainting due to the lack of oxygen. To prevent this, the cryosauna is designed to keep the patient's head above the chamber, and patients are instructed to breathe up room-air.</p>
    </div>

    <div class="faq" style="top:446px">
      <svg class="faq__icon" width="22" height="18" viewBox="0 0 22 18"><path d="M2 1h14a2 2 0 0 1 2 2v7a2 2 0 0 1-2 2H8l-4 4v-4H2a2 2 0 0 1-2-2V3a2 2 0 0 1 2-2z" fill="var(--violet)"/><circle cx="6" cy="7" r="1.2" fill="#fff"/><circle cx="9.5" cy="7" r="1.2" fill="#fff"/><circle cx="13" cy="7" r="1.2" fill="#fff"/></svg>
      <h3 class="faq__q">Is it comfortable?</h3>
      <p class="faq__a">Whereas an ice bath has direct contact with the skin and can be painful, cryotherapy is a dry, indirect contact. Due to the session only being three minutes max, the session is very tolerable. Towards the end of the session, you may get a tiny "pins and needles" sensation, which disappears immediately after the treatment.</p>
    </div>
  </div>

  <div class="panel panel--2" style="background:linear-gradient(180deg,var(--navy) 0%,var(--deep) 100%)">
    <div class="photo" role="img" aria-label="Illustration of a human body showing muscles and skeleton in blue with red joint highlights" style="left:0;top:0;width:100%;height:330px;background:radial-gradient(ellipse at 45% 40%,#5d8ff0 0%,#2c5fd6 40%,#1a3fa8 75%,#0f2d86 100%)"></div>
    <svg class="wave" style="top:250px" width="247" height="130" viewBox="0 0 247 130">
      <path d="M0 70 C80 80 170 40 247 0 L247 130 L0 130Z" fill="var(--navy)"/>
      <path d="M0 62 C80 72 170 32 247 -8" stroke="var(--sky)" stroke-width="10" fill="none"/>
      <path d="M0 74 C80 84 170 44 247 4" stroke="#fff" stroke-width="3" fill="none"/>
    </svg>
    <div style="position:absolute;left:34px;top:268px;width:178px;height:78px;border-radius:50%;background:var(--white);border:4px solid var(--navy);box-shadow:0 0 0 3px var(--sky);display:flex;align-items:center;justify-content:center">
      <div class="brand" style="font-size:10px;gap:5px"><span class="brand__dot" style="width:12px;height:12px"></span>Tidewell Cryotherapy</div>
    </div>
    <ul class="contact">
      <li><svg width="9" height="11" viewBox="0 0 9 11"><path d="M4.5 0A4.5 4.5 0 0 0 0 4.5C0 8 4.5 11 4.5 11S9 8 9 4.5A4.5 4.5 0 0 0 4.5 0z" fill="#fff"/><circle cx="4.5" cy="4.5" r="1.6" fill="var(--navy)"/></svg>123 your address location</li>
      <li><svg width="10" height="8" viewBox="0 0 10 8"><rect width="10" height="8" rx="1" fill="#fff"/><path d="M0 0l5 4 5-4" stroke="var(--navy)" fill="none"/></svg>info@emailid.com</li>
      <li><svg width="9" height="9" viewBox="0 0 9 9"><path d="M2 0l1.5 2.2-1 1.3a6 6 0 0 0 3 3l1.3-1L9 7 7.5 9C3.5 9 0 5.5 0 1.5z" fill="#fff"/></svg>1234567890</li>
      <li><svg width="9" height="9" viewBox="0 0 9 9"><circle cx="4.5" cy="4.5" r="4" stroke="#fff" fill="none"/><path d="M0.5 4.5h8M4.5 0.5c-2 2.5-2 5.5 0 8M4.5 0.5c2 2.5 2 5.5 0 8" stroke="#fff" fill="none" stroke-width=".8"/></svg>www.websitename.com</li>
    </ul>
  </div>

  <div class="panel panel--3" style="background:linear-gradient(180deg,#fff 0%,#fff 60%,#e4e6ea 75%,#fff 85%)">
    <div class="brand" style="position:absolute;top:28px;left:46px;font-size:11px"><span class="brand__dot"></span>Tidewell Cryotherapy</div>
    <svg class="wave" style="top:66px" width="247" height="20" viewBox="0 0 247 20">
      <path d="M0 16 C80 4 170 2 247 6" stroke="var(--navy)" stroke-width="5" fill="none"/>
    </svg>
    <div class="photo" role="img" aria-label="Photo of a full body cryotherapy chamber lit in blue" style="left:0;top:76px;width:100%;height:262px;clip-path:ellipse(130% 100% at 60% 0%);background:linear-gradient(120deg,#e8ecf2 0%,#c4ccd8 35%,#5b7fd8 55%,#2d3b6e 75%,#c9cfd8 100%)"></div>
    <svg class="wave" style="top:290px" width="247" height="70" viewBox="0 0 247 70">
      <path d="M0 6 C60 40 160 50 247 40" stroke="var(--navy)" stroke-width="5" fill="none"/>
      <path d="M0 16 C60 50 160 60 247 50" stroke="var(--silver)" stroke-width="6" fill="none"/>
    </svg>
    <div class="cover-title">
      <div class="cover-title__main">WHOLE BODY</div>
      <div class="cover-title__sub">CRYOTHERAPY</div>
    </div>
    <svg class="wave" style="top:470px" width="247" height="102" viewBox="0 0 247 102">
      <path d="M0 30 C90 0 170 10 247 20 L247 102 L0 102Z" fill="var(--sky)"/>
      <path d="M0 50 C90 20 170 30 247 40 L247 102 L0 102Z" fill="var(--navy)"/>
    </svg>
  </div>
</section>

<section class="spread spread--inside" aria-label="Brochure inside">
  <div class="panel panel--1" style="background:linear-gradient(170deg,var(--deep) 0%,var(--navy) 55%,var(--sky) 100%)">
    <div class="block" style="top:28px;left:0;width:100%">
      <h2 class="tab tab--light">About Full Body Cryotherapy</h2>
      <p class="copy copy--light" style="padding:8px 14px 0 18px;text-align:justify">Lorem Ipsum is simply dummy text of the printing and typesetting industry. Lorem Ipsum has been the industry's standard dummy text ever since the 1500s, when an unknown printer took a galley of type and scrambled it to make a type specimen book. It has survived not only five centuries, but also the leap into electronic typesetting, remaining essentially unchanged. It was popularised in the 1960s with the release of Tracemark sheets containing Lorem Ipsum passages, and more recently with desktop publishing software like Quillpress Layout including versions of Lorem Ipsum.</p>
    </div>
    <div class="block" style="top:196px;left:0;width:100%">
      <h2 class="tab tab--light" style="padding-left:20px">Benefits of Full Body Cryotherapy</h2>
      <ul class="bullets bullets--light" style="padding:10px 14px 0 18px">
        <li>Lorem Ipsum is simply dummy text of the printing and typesetting industry.</li>
        <li>Lorem Ipsum has been the industry's standard dummy text ever since the 1500s, when an unknown printer took a galley of type and scrambled it to make a type specimen book.</li>
        <li>It has survived not only five centuries, but also the leap into electronic typesetting, remaining essentially unchanged. It was popularised in the 1960s with the release of Tracemark sheets containing</li>
        <li>Lorem Ipsum passages, and more recently with desktop publishing software like Quillpress Layout including versions of Lorem Ipsum.</li>
      </ul>
    </div>
    <div class="photo" role="img" aria-label="Photo of clients in white robes beside a cryotherapy chamber with cold vapour" style="left:22px;top:440px;width:250px;height:220px;border-radius:50%;border:4px solid var(--white);background:radial-gradient(ellipse at 40% 40%,#f4f7fd 0%,#c9d6f0 45%,#6e8fd8 80%,#3556b8 100%)"></div>
  </div>

  <div class="panel panel--2" style="background:var(--white)">
    <svg class="wave" style="top:0" width="247" height="40" viewBox="0 0 247 40">
      <path d="M0 0 L247 0 L247 10 C160 30 70 8 0 22Z" fill="var(--navy)"/>
    </svg>
    <div class="block" style="top:30px;left:0;width:100%">
      <h2 class="tab tab--dark" style="margin-left:18px;border-radius:12px">Our Services</h2>
      <ul class="bullets bullets--dark" style="padding:10px 14px 0 28px">
        <li>Lorem Ipsum is simply dummy text of the printing and typesetting industry.</li>
        <li>Lorem Ipsum has been the industry's standard dummy text ever since the 1500s, when an unknown printer took a galley of type and scrambled it to make a type specimen book.</li>
        <li>It has survived not only five centuries, but also the leap into electronic typesetting, remaining essentially unchanged. It was popularised in the 1960s with the release of Tracemark sheets containing</li>
        <li>Lorem Ipsum passages, and more recently with desktop publishing software like Quillpress Layout including versions of Lorem Ipsum.</li>
        <li>It was popularised in the 1960s with the release of Tracemark sheets containing</li>
      </ul>
    </div>
    <div class="photo" role="img" aria-label="Photo of a woman receiving a facial cryotherapy treatment with cold mist and red laser light" style="left:0;top:290px;width:100%;height:282px;clip-path:ellipse(140% 100% at 100% 100%);background:linear-gradient(160deg,#d6deee 0%,#8fa6cf 30%,#3a4f86 55%,#e9d2c2 80%,#b99684 100%)"></div>
    <svg class="wave" style="top:272px" width="247" height="60" viewBox="0 0 247 60">
      <path d="M0 58 C60 20 160 8 247 14" stroke="var(--navy)" stroke-width="4" fill="none"/>
    </svg>
  </div>

  <div class="panel panel--3" style="background:linear-gradient(180deg,var(--sky) 0%,#1f8fd0 50%,var(--sky) 100%)">
    <div class="block" style="top:40px;left:14px;width:218px">
      <h2 class="tab tab--dark" style="border-radius:12px">Prices for Cryotherapy</h2>
      <ul class="rates" style="margin-top:8px">
        <li>Lorem Ipsum is simply dummy text<span>$00.00</span></li>
        <li>Lorem Ipsum is simply dummy text<span>$00.00</span></li>
        <li>Lorem Ipsum is simply dummy text<span>$00.00</span></li>
        <li>Lorem Ipsum is simply dummy text<span>$00.00</span></li>
        <li>Lorem Ipsum is simply dummy text<span>$00.00</span></li>
        <li>Lorem Ipsum is simply dummy text<span>$00.00</span></li>
        <li>Lorem Ipsum is simply dummy text<span>$00.00</span></li>
      </ul>
    </div>
    <svg class="wave" style="top:150px" width="247" height="80" viewBox="0 0 247 80">
      <path d="M0 70 C80 40 170 20 247 2" stroke="var(--navy)" stroke-width="10" fill="none"/>
      <path d="M0 78 C80 48 170 28 247 10" stroke="#fff" stroke-width="3" fill="none"/>
    </svg>
    <div class="photo" role="img" aria-label="Photo of a woman wrapped in a white towel, eyes closed, relaxing" style="left:48px;top:198px;width:150px;height:150px;border-radius:50%;border:4px solid var(--navy);box-shadow:0 0 0 3px var(--white);background:radial-gradient(circle at 50% 40%,#f1e4d8 0%,#d7c2b0 35%,#5d7fc4 70%,#2a4aa6 100%)"></div>
    <svg class="wave" style="top:360px" width="247" height="60" viewBox="0 0 247 60">
      <path d="M0 50 C80 30 170 14 247 4" stroke="var(--navy)" stroke-width="4" fill="none"/>
    </svg>
    <div class="block" style="top:398px;left:14px;width:218px">
      <h2 class="tab tab--dark" style="border-radius:12px">Hours for Cryotherapy</h2>
      <ul class="rates" style="margin-top:8px">
        <li>Lorem Ipsum is simply dummy text<span>00.00</span></li>
        <li>Lorem Ipsum is simply dummy text<span>00.00</span></li>
        <li>Lorem Ipsum is simply dummy text<span>00.00</span></li>
        <li>Lorem Ipsum is simply dummy text<span>00.00</span></li>
        <li>Lorem Ipsum is simply dummy text<span>00.00</span></li>
      </ul>
    </div>
  </div>
</section>

</body>
</html>
```